New Business Card Design Project VORASTI-Italy

we are VORASTI-Italy
our company in the market for 3 years we are luxury cosmetic company and its about time for a facelift :)
i will like to have elegant luxurious and unique business card
that will give the person that get it a unique, luxurious and elegant impression
I'm VERY OPEN FOR NEW IDEAS , even duo i add a few files of things that i see on line and i like them

i add my logo as well
my website is VORASTI.COM
(if you would like to see the main style that we have)

Target Market(s)

adult that have money :)

Industry/Entity Type

Business

Contact Information for Business Card

Name - Paul Vorasti
Position - CEO and CO Founder
address - 4817 E Larkdale
telephone - 555-384-1962
email - paul@vorasti.com
fax - 555-384-1962
website - VORASTI.COM

Colors
000000
959595
fbee3e
ffffff

Requirements
Must have
• big logo in GOLD color
• elegant look
• impressive
Nice to have
• not must but maybe classy pattern background
• not must but maybe emblem
• maybe clear plastic business card
Should not have
• colors
• images

```html
<!DOCTYPE html>
<html lang="en">
<head>
<meta charset="utf-8">
<title>VORASTI-Italy Business Card</title>
<link href="https://fonts.googleapis.com/css2?family=Crimson+Pro:wght@400;500&display=swap" rel="stylesheet">
<style>
  :root {
    --stage: #2b2b2b;
    --card-black: #030608;
    --card-white: #ffffff;
    --gold: #c9a63f;
    --ink-grey: #7a7a7a;
  }
  html, body {
    margin: 0;
    padding: 0;
    width: 1200px;
    height: 864px;
    overflow: hidden;
    background: var(--stage);
    font-family: "Crimson Pro", "Times New Roman", serif;
  }
  .card {
    position: absolute;
    top: 291px;
    width: 492px;
    height: 281px;
    box-shadow: 0 6px 14px rgba(0,0,0,0.55);
  }
  .card--front { left: 99px; background: var(--card-black); }
  .card--back  { left: 609px; background: var(--card-white); }

  .brand {
    position: absolute;
    display: flex;
    flex-direction: column;
    align-items: center;
    transform: translateX(-50%);
  }
  .brand__mark {
    border: 2px solid var(--gold);
    border-radius: 50%;
    box-sizing: border-box;
  }
  .brand__name {
    color: var(--gold);
    font-weight: 400;
    line-height: 1;
    letter-spacing: 0.5px;
  }
  .card--front .brand { left: 246px; top: 62px; }
  .card--front .brand__mark { width: 80px; height: 80px; margin-bottom: 18px; }
  .card--front .brand__name { font-size: 36px; }

  .card--back .brand { left: 142px; top: 70px; }
  .card--back .brand__mark { width: 74px; height: 74px; margin-bottom: 16px; }
  .card--back .brand__name { font-size: 32px; }

  .divider {
    position: absolute;
    left: 261px;
    top: 58px;
    width: 1.5px;
    height: 166px;
    background: var(--gold);
  }
  .details {
    position: absolute;
    left: 296px;
    top: 52px;
    color: var(--ink-grey);
    font-size: 15px;
    line-height: 1.2;
  }
  .details__name { color: var(--gold); font-size: 21px; font-weight: 500; margin: 0; line-height: 1.1; }
  .details__role { margin: 0 0 12px; }
  .details__company { color: var(--gold); font-weight: 500; margin: 0; }
  .details__address { margin: 0 0 10px; }
  .contact { list-style: none; margin: 0; padding: 0; }
  .contact li { display: flex; align-items: center; gap: 5px; height: 18px; }
  .contact svg { width: 12px; height: 12px; fill: var(--gold); flex: none; }
</style>
</head>
<body>
  <section class="card card--front" aria-label="Card front">
    <div class="brand">
      <div class="brand__mark"></div>
      <div class="brand__name">VORASTI</div>
    </div>
  </section>

  <section class="card card--back" aria-label="Card back">
    <div class="brand">
      <div class="brand__mark"></div>
      <div class="brand__name">VORASTI</div>
    </div>
    <div class="divider"></div>
    <div class="details">
      <p class="details__name">Paul Vorasti</p>
      <p class="details__role">CEO and CO Founder</p>
      <p class="details__company">VORASTI-Italy</p>
      <p class="details__address">4817 E Larkdale</p>
      <ul class="contact">
        <li><svg viewBox="0 0 12 12" aria-hidden="true"><path d="M2 1l2.5 0 1 3-1.5 1a6 6 0 0 0 3 3l1-1.5 3 1V11a1 1 0 0 1-1 1A10 10 0 0 1 1 2a1 1 0 0 1 1-1z"/></svg>555-384-1962</li>
        <li><svg viewBox="0 0 12 12" aria-hidden="true"><path d="M3 1h6v3H3zM1 5h10v5H9V8H3v2H1zM3 9h6v3H3z"/></svg>555-384-1962</li>
        <li><svg viewBox="0 0 12 12" aria-hidden="true"><path d="M0 3h12v7H0zM0 3l6 4 6-4v1L6 8 0 4z" fill-rule="evenodd"/></svg>paul@vorasti.com</li>
        <li><svg viewBox="0 0 12 12" aria-hidden="true"><path d="M6 0.5a5.5 5.5 0 1 0 0 11a5.5 5.5 0 1 0 0-11zm0 1c-1 1-1.5 2.5-1.6 4h3.2C7.5 4 7 2.5 6 1.5zM1.6 5.5h1.8c.1-1.4.5-2.7 1.2-3.7A4.5 4.5 0 0 0 1.6 5.5zm8.8 0A4.5 4.5 0 0 0 7.4 1.8c.7 1 1.1 2.3 1.2 3.7zM1.6 6.5a4.5 4.5 0 0 0 3 3.7c-.7-1-1.1-2.3-1.2-3.7zm2.8 0c.1 1.5.6 3 1.6 4 1-1 1.5-2.5 1.6-4zm4.2 0c-.1 1.4-.5 2.7-1.2 3.7a4.5 4.5 0 0 0 3-3.7z"/></svg>VORASTI.COM</li>
      </ul>
    </div>
  </section>
</body>
</html>
```